NZ First of it's kind solutions directory and marketplace for busy Mums needs a business card design

We need a business card design for our new nationwide business in NZ (long term plans to go global). We provide solutions to the everyday challenges that busy Mums face by connecting them with quality communities and suppliers of carefully selected, relevant products and services. We sell direct via our online marketplace. The final design should communicate our values of inclusivity, quality and smart solutions. Colours should incorporate our logo colour palette of #477077 and #6ba8b2. Our website is at https://www.brightnestly.com

Target Market(s)

busy Mums, Age 28 – 50, female, income over $100K, location main centres NZ primarily but NZ wide. Is likely juggling work or career with a young family. Probably had hobbies which have fallen by the wayside.
-Wants to succeed in her chosen career without compromising on family life
-to successfully juggle her career without feeling like she is compromising her children
- Is time poor, something always has to give and it’s generally her health (she’ll stay up late, get stressed)
- probably ex corporate or professional career. Has discretional income

Industry/Entity Type

Business

Contact Information for Business Card

Jodie Farnsworth, Founder, BrightNestly.com (Strapline Browse; Pick; Sorted), 48 Kowhai Terrace, Hillsborough, Auckland 1058, New Zealand. Mob: 021 437 518 Ph: +64 (0)9 584 7163

Font styles to use
Other font styles liked:
• Raleway, and/or Architects Daughter

Colors
00a990
33b8a4
86cfc6
cfeae6

Requirements
Must have
• the above details, streamline. the logo and colours associated with those logos
Should not have
• foil or metallic colours

```html
<!DOCTYPE html>
<html lang="en">
<head>
<meta charset="utf-8">
<title>BrightNestly Business Card</title>
<link rel="stylesheet" href="https://fonts.googleapis.com/css2?family=Signika:wght@600&family=Roboto:ital,wght@0,400;1,400&display=swap">
<style>
  :root {
    --brand-deep: #3d5f66;
    --brand-primary: #477077;
    --brand-light: #6ba8b2;
    --ink: #3b3b3b;
    --card: #f8f8f7;
    --backdrop: #e6e6e6;
  }
  * { margin: 0; padding: 0; box-sizing: border-box; }
  html, body {
    width: 1200px;
    height: 576px;
    overflow: hidden;
    background: var(--backdrop);
  }
  .stage {
    position: relative;
    width: 1200px;
    height: 576px;
  }
  .card {
    position: absolute;
    top: 138px;
    width: 484px;
    height: 294px;
    background: var(--card);
    border-radius: 14px;
    overflow: hidden;
    box-shadow: 0 1px 3px rgba(0,0,0,0.18);
  }
  .card--front { left: 82px; }
  .card--back { left: 602px; }

  .brand-name {
    font-family: "Signika", sans-serif;
    font-weight: 600;
    color: var(--brand-primary);
    letter-spacing: -0.5px;
    line-height: 1;
    white-space: nowrap;
  }
  .tagline {
    font-family: "Roboto", sans-serif;
    color: var(--ink);
    text-transform: uppercase;
    white-space: nowrap;
  }
  .tagline .divider { color: var(--brand-light); }

  /* Front */
  .front-disc {
    position: absolute;
    left: 10px;
    top: 100px;
    width: 180px;
    height: 180px;
    border-radius: 50%;
    background: var(--brand-deep);
  }
  .card--front .brand-name {
    position: absolute;
    left: 213px;
    top: 198px;
    font-size: 37px;
  }
  .card--front .tagline {
    position: absolute;
    left: 214px;
    top: 240px;
    font-size: 10.5px;
    letter-spacing: 3.6px;
  }

  /* Back */
  .back-brand {
    position: absolute;
    left: 40px;
    top: 98px;
    width: 188px;
    text-align: center;
  }
  .back-disc {
    width: 40px;
    height: 40px;
    margin: 0 auto 14px;
    border-radius: 50%;
    background: var(--brand-deep);
  }
  .back-brand .brand-name { font-size: 28px; }
  .back-brand .tagline {
    margin-top: 9px;
    font-size: 8px;
    letter-spacing: 2.9px;
  }

  .contact {
    position: absolute;
    left: 264px;
    top: 56px;
    font-family: "Roboto", sans-serif;
    color: var(--ink);
  }
  .contact__name {
    font-family: "Signika", sans-serif;
    font-weight: 600;
    font-size: 19px;
    color: var(--brand-primary);
    line-height: 1.1;
  }
  .contact__role {
    font-style: italic;
    font-size: 11.5px;
    margin-top: 4px;
  }
  .contact__address {
    font-size: 11.5px;
    line-height: 18px;
    margin-top: 16px;
    font-style: normal;
  }
  .contact__list {
    list-style: none;
    margin-top: 11px;
    font-size: 11.5px;
  }
  .contact__list li {
    display: flex;
    align-items: center;
    height: 18.5px;
  }
  .contact__list svg {
    width: 10px;
    height: 10px;
    margin-right: 8px;
    fill: var(--brand-primary);
    flex: none;
  }
</style>
</head>
<body>
<main class="stage">

  <section class="card card--front" aria-label="Business card front">
    <div class="front-disc"></div>
    <p class="brand-name">BrightNestly</p>
    <p class="tagline">Browse <span class="divider">|</span> Pick <span class="divider">|</span> Sorted</p>
  </section>

  <section class="card card--back" aria-label="Business card back">
    <div class="back-brand">
      <div class="back-disc"></div>
      <p class="brand-name">BrightNestly</p>
      <p class="tagline">Browse <span class="divider">|</span> Pick <span class="divider">|</span> Sorted</p>
    </div>

    <div class="contact">
      <p class="contact__name">Jodie Farnsworth</p>
      <p class="contact__role">Founder</p>
      <address class="contact__address">48 Kowhai Terrace, Hillsborough,<br>Auckland 1058, New Zealand</address>
      <ul class="contact__list">
        <li>
          <svg viewBox="0 0 10 10" aria-hidden="true"><path d="M2.5 0h5a1 1 0 0 1 1 1v8a1 1 0 0 1-1 1h-5a1 1 0 0 1-1-1V1a1 1 0 0 1 1-1zm0 1.5v6h5v-6zM5 8.2a.5.5 0 1 0 0 1 .5.5 0 0 0 0-1z"/></svg>
          021 437 518
        </li>
        <li>
          <svg viewBox="0 0 10 10" aria-hidden="true"><path d="M0 3c0-1.3 2.2-2.2 5-2.2S10 1.7 10 3v1H7.5V3h-5v1H0zM2 5h6l1.5 4.5h-9zm3 .8a1.3 1.3 0 1 0 0 2.6 1.3 1.3 0 0 0 0-2.6z"/></svg>
          +64 (0)9 584 7163
        </li>
        <li>
          <svg viewBox="0 0 10 10" aria-hidden="true"><path d="M0 2h10v.6L5 5.8 0 2.6zm0 1.7l5 3.2 5-3.2V8H0z"/></svg>
          www.BrightNestly.com
        </li>
        <li>
          <svg viewBox="0 0 10 10" aria-hidden="true"><path d="M5 0a5 5 0 1 0 0 10A5 5 0 0 0 5 0zm0 .9c.6.5 1.1 1.6 1.3 3.1H3.7C3.9 2.5 4.4 1.4 5 .9zM1 4.6h1.9c0 .3 0 .6 0 .8H1a4 4 0 0 1 0-.8zm2.7 0h2.6v.8H3.7zm3.4 0H9a4 4 0 0 1 0 .8H7.1zM3.7 6h2.6C6.1 7.5 5.6 8.6 5 9.1 4.4 8.6 3.9 7.5 3.7 6z"/></svg>
          jodie@brightnestly.com
        </li>
      </ul>
    </div>
  </section>

</main>
</body>
</html>
```